Bay Area SaaS Company needs brochure for new Quality Management System (QMS) product offering

Velmarcor (www.velmarcor-example.com) is a bay area SaaS company. We have developed a new product, a Quality Management System or QMS for short.

We have assembled the bulk text & content in a word file (attached), along with a few logos to support the key features list.

What we essentially need is for somebody to take the attached document and turn it into a professional looking digital brochure.

Brochure layout:
Headline:
Product Summary:
Key Features:
Call to action:

```html
<!DOCTYPE html>
<html lang="en">
<head>
<meta charset="utf-8">
<title>QMS – Quality Management System Brochure</title>
<link rel="stylesheet" href="https://fonts.googleapis.com/css2?family=Inter:wght@300;400;600;700&display=swap">
<style>
  :root {
    --hero-bg: #e7e8ea;
    --band-grey: #636466;
    --brand-red: #e32b26;
    --ink: #231f20;
    --muted-grey: #8a8b8d;
    --stripe-grey: #c9cacc;
    --icon-grey: #b8b9bb;
    --white: #ffffff;
  }
  * { box-sizing: border-box; margin: 0; padding: 0; }
  html, body { width: 848px; height: 1200px; overflow: hidden; background: var(--white); }
  body { font-family: "Inter", Helvetica, Arial, sans-serif; color: var(--ink); }
  .brochure { position: relative; width: 848px; height: 1200px; overflow: hidden; background: var(--white); }

  .hero { position: absolute; left: 0; top: 0; width: 848px; height: 379px; background: var(--hero-bg); overflow: hidden; }
  .hero-stripes { position: absolute; left: 0; top: 0; }
  .hero-photo {
    position: absolute; left: 410px; top: 40px; width: 438px; height: 339px;
    background: radial-gradient(ellipse at 38% 42%, #e63a45 0 14%, transparent 15%),
                radial-gradient(ellipse at 75% 40%, #f3ecd2 0 22%, transparent 40%),
                linear-gradient(120deg, var(--hero-bg) 0%, #eeeeec 55%, #f1eedf 100%);
  }
  .hero-title { position: absolute; left: 52px; top: 152px; font-size: 88px; font-weight: 300; letter-spacing: -2px; line-height: 1; color: #111; }
  .hero-subtitle { position: absolute; left: 58px; top: 266px; font-size: 22px; line-height: 30px; color: var(--muted-grey); font-weight: 400; }
  .hero-subtitle strong { font-weight: 700; }

  .summary-band { position: absolute; left: 0; top: 379px; width: 848px; height: 104px; background: var(--band-grey); overflow: hidden; }
  .summary-band p { position: absolute; left: 58px; top: 9px; width: 720px; font-size: 16.4px; line-height: 21.3px; color: var(--white); font-weight: 300; letter-spacing: -0.1px; }
  .summary-stripes { position: absolute; right: 0; top: 0; }
  .red-rule { position: absolute; left: 0; top: 483px; width: 848px; height: 9px; background: var(--brand-red); }

  .feature { position: absolute; width: 228px; }
  .feature-icon { display: block; height: 44px; }
  .feature-title { margin-top: 10px; font-size: 13px; line-height: 16px; font-weight: 700; color: var(--brand-red); letter-spacing: -0.1px; }
  .feature-body { margin-top: 4px; font-size: 11.6px; line-height: 14.6px; font-weight: 400; letter-spacing: -0.15px; }
  .col-1 { left: 51px; } .col-2 { left: 318px; } .col-3 { left: 590px; }
  .row-1 { top: 508px; } .row-2 { top: 728px; } .row-3 { top: 900px; }
  .brand-wordmark { height: 44px; font-size: 20px; font-weight: 700; color: var(--ink); padding-top: 8px; }

  .cta-band { position: absolute; left: 0; top: 1090px; width: 848px; height: 110px; }
  .cta-text { position: absolute; left: 51px; top: 1145px; font-size: 13px; line-height: 22px; color: var(--white); font-weight: 300; white-space: nowrap; }
  .cta-text strong { font-weight: 600; font-size: 13.6px; letter-spacing: -0.2px; }
  .company-name { position: absolute; left: 640px; top: 1136px; font-size: 26px; font-weight: 400; color: var(--brand-red); letter-spacing: -0.5px; }
</style>
</head>
<body>
<main class="brochure">
  <header class="hero">
    <svg class="hero-stripes" width="360" height="150" viewBox="0 0 360 150" aria-hidden="true">
      <polygon points="113,18 170,18 257,85 200,85" fill="var(--stripe-grey)"/>
      <polygon points="107,0 178,0 258,85 187,85" fill="var(--brand-red)"/>
      <polygon points="210,0 262,0 360,122 308,122" fill="var(--stripe-grey)" opacity=".6"/>
      <line x1="207" y1="20" x2="330" y2="145" stroke="var(--white)" stroke-width="1.5"/>
    </svg>
    <div class="hero-photo" role="img" aria-label="Photo of a red paper boat leading a fleet of cream paper boats"></div>
    <h1 class="hero-title">QMS</h1>
    <p class="hero-subtitle">The Ultimate<br><strong>Quality Management System</strong><br>for DocuPoint Has Arrived</p>
  </header>

  <section class="summary-band">
    <p>QMS is a next-generation quality management system<br>that enables unprecedented levels of transparency, collaboration and approval process<br>within all phases quality management and the team to execute integrations<br>to digitally transform your organization.</p>
    <svg class="summary-stripes" width="160" height="104" viewBox="0 0 160 104" aria-hidden="true">
      <polygon points="0,-10 40,-10 140,90 100,90" fill="#4f5052"/>
      <polygon points="60,-10 120,-10 160,30 160,104 150,104" fill="#8c8d8f" opacity=".7"/>
    </svg>
  </section>
  <div class="red-rule"></div>

  <article class="feature col-1 row-1">
    <svg class="feature-icon" width="44" height="44" viewBox="0 0 44 44" aria-hidden="true">
      <circle cx="20" cy="16" r="15" fill="var(--icon-grey)"/>
      <rect x="2" y="34" width="36" height="7" fill="var(--ink)"/>
    </svg>
    <h2 class="feature-title">ISO 9001:2015 Focused</h2>
    <p class="feature-body">QMS adheres to the highest level of international standards – QMS, is an ISO 9001:2015 process-based quality management system centered around risk-based thinking &amp; features automated sequential reviews &amp; approvals processes associated with the ISO “Plan-Do-Check Act” standard</p>
  </article>

  <article class="feature col-2 row-1">
    <svg class="feature-icon" width="46" height="44" viewBox="0 0 46 44" aria-hidden="true">
      <rect x="0" y="32" width="6" height="12" fill="var(--icon-grey)"/>
      <rect x="10" y="26" width="6" height="18" fill="var(--icon-grey)"/>
      <rect x="20" y="20" width="6" height="24" fill="var(--icon-grey)"/>
      <rect x="30" y="14" width="6" height="30" fill="var(--icon-grey)"/>
      <polyline points="1,17 12,9 22,15 42,2" fill="none" stroke="var(--ink)" stroke-width="1.8"/>
      <polygon points="44,0 37,1 42,7" fill="var(--ink)"/>
    </svg>
    <h2 class="feature-title">Advanced Progress Tracking</h2>
    <p class="feature-body">QMS delivers advanced progress-tracking for any quality record while providing stakeholders with real time transactional alerts at every decision point. This ensures stakeholders within the quality management team always receive approval tasks on time &amp; in the correct order.</p>
  </article>

  <article class="feature col-3 row-1">
    <svg class="feature-icon" width="40" height="44" viewBox="0 0 40 44" aria-hidden="true">
      <g fill="none" stroke="var(--ink)" stroke-width="1.6">
        <polygon points="20,2 38,11 20,20 2,11" fill="var(--white)"/>
        <polyline points="2,19 20,28 38,19"/>
        <polyline points="2,27 20,36 38,27"/>
      </g>
    </svg>
    <h2 class="feature-title">Middleware Integration</h2>
    <p class="feature-body">Powerful APIs allow QMS to act as a middleware solution to existing legacy systems. By doing so, QMS greatly improves QM by providing automated &amp; fully ISO 9001:2015 compliant review &amp; approval process &amp; quality audit suite functionality.</p>
  </article>

  <article class="feature col-1 row-2">
    <svg class="feature-icon" width="50" height="36" viewBox="0 0 50 36" aria-hidden="true">
      <path d="M10 32 H42 A7 7 0 0 0 42 18 A10 10 0 0 0 24 10 A8 8 0 0 0 11 18 A7 7 0 0 0 10 32 Z" fill="var(--icon-grey)" transform="translate(3,2)"/>
      <path d="M10 32 H42 A7 7 0 0 0 42 18 A10 10 0 0 0 24 10 A8 8 0 0 0 11 18 A7 7 0 0 0 10 32 Z" fill="none" stroke="var(--ink)" stroke-width="1.6"/>
    </svg>
    <h2 class="feature-title">Cloud &amp; On Premises</h2>
    <p class="feature-body">QMS is available as a hosted cloud service, &amp; can also be integrated into existing on premises environments, including DocuPoint 2016 &amp; 2019.</p>
  </article>

  <article class="feature col-2 row-2">
    <svg class="feature-icon" width="70" height="36" viewBox="0 0 70 36" aria-hidden="true">
      <g fill="none" stroke="var(--ink)" stroke-width="1.4">
        <circle cx="5" cy="13" r="4"/>
        <line x1="9" y1="13" x2="17" y2="13"/>
        <polygon points="23,7 29,13 23,19 17,13"/>
        <polyline points="23,7 23,3 45,3 45,9"/>
        <polyline points="29,13 41,13"/>
        <polyline points="23,19 23,23 45,23"/>
        <line x1="45" y1="17" x2="45" y2="27"/>
        <rect x="42" y="27" width="7" height="7"/>
        <line x1="49" y1="13" x2="61" y2="13"/>
        <circle cx="65" cy="13" r="4"/>
      </g>
      <rect x="41" y="9" width="8" height="8" fill="var(--ink)"/>
    </svg>
    <h2 class="feature-title">Automated Workflow Processes</h2>
    <p class="feature-body">Workflow processes, interrelationships, &amp; interdependencies are uniquely presented in a simple &amp; user-friendly interface &amp; ensures that no critical steps are overlooked.</p>
  </article>

  <article class="feature col-3 row-2">
    <svg class="feature-icon" width="34" height="36" viewBox="0 0 34 36" aria-hidden="true">
      <path d="M6 2 H22 L30 10 V34 H6 Z" fill="var(--icon-grey)" transform="translate(2,-1)"/>
      <path d="M2 2 H20 L26 8 V34 H2 Z" fill="var(--white)" stroke="var(--ink)" stroke-width="1.4"/>
      <g stroke="var(--ink)" stroke-width="1.3">
        <line x1="6" y1="16" x2="16" y2="16"/><line x1="6" y1="20" x2="14" y2="20"/>
        <line x1="6" y1="24" x2="14" y2="24"/><line x1="6" y1="28" x2="16" y2="28"/>
      </g>
      <circle cx="22" cy="24" r="5" fill="var(--white)" stroke="var(--ink)" stroke-width="1.5"/>
      <line x1="26" y1="28" x2="32" y2="34" stroke="var(--ink)" stroke-width="2"/>
    </svg>
    <h2 class="feature-title">Built-In Audit Trails</h2>
    <p class="feature-body">QMS features built-in audit trails history functionality. This ensures that the system complies with all major quality compliance &amp; regulatory requirements.</p>
  </article>

  <article class="feature col-1 row-3">
    <svg class="feature-icon" width="56" height="36" viewBox="0 0 56 36" aria-hidden="true">
      <path d="M4 2 H24 V8 H18 V30 H10 V8 H4 Z" fill="var(--icon-grey)" transform="translate(2,0)"/>
      <path d="M4 2 H24 V8 H18 V30 H10 V8 H4 Z" fill="none" stroke="var(--ink)" stroke-width="1.4"/>
      <rect x="2" y="33" width="26" height="3" fill="var(--ink)"/>
      <path d="M34 31 L50 15 L54 19 L38 35 L32 36 Z" fill="none" stroke="var(--ink)" stroke-width="1.4"/>
    </svg>
    <h2 class="feature-title">Single-source-of-truth</h2>
    <p class="feature-body">QMS offers normalization &amp; annotation of over 450 file types, embedding of thumbnails, &amp; intuitive viewing of all files, without the need for plug-ins, downloads, synching or other software applications. This enables all files to be centralized &amp; viewable in-place to dramatically change the user experience.</p>
  </article>

  <article class="feature col-2 row-3">
    <div class="brand-wordmark">AssetVault</div>
    <h2 class="feature-title">Complete Integration of full Digital Asset Management features</h2>
    <p class="feature-body">Centralized viewing in-place, batch uploading, &amp; batch tagging of assets is just the beginning. The QM System is built on a full-fledged digital asset management system &amp; technology used by companies like the Northfield Energy Agency &amp; Civic Works Office.</p>
  </article>

  <article class="feature col-3 row-3">
    <svg class="feature-icon" width="36" height="36" viewBox="0 0 36 36" aria-hidden="true">
      <rect x="5" y="8" width="28" height="26" rx="3" fill="var(--icon-grey)"/>
      <rect x="2" y="6" width="28" height="26" rx="3" fill="none" stroke="var(--ink)" stroke-width="1.8"/>
      <line x1="12" y1="22" x2="30" y2="5" stroke="var(--ink)" stroke-width="3"/>
      <polygon points="34,0 24,1 33,10" fill="var(--ink)"/>
    </svg>
    <h2 class="feature-title">Planmark link extraction and ViewFlow™ technology</h2>
    <p class="feature-body">By creating a simple universal viewing experience with annotation capabilities, it’s possible to give real-time feedback on any document, incident report, image or video file.</p>
  </article>

  <svg class="cta-band" width="848" height="110" viewBox="0 0 848 110" aria-hidden="true">
    <polygon points="432,0 470,0 590,110 552,110" fill="#dcdddf"/>
    <polygon points="480,5 510,5 615,110 585,110" fill="#c4c5c7"/>
    <polygon points="0,43 552,43 594,110 0,110" fill="var(--band-grey)"/>
  </svg>
  <p class="cta-text">If you are interested in learning more about QMS<br>please visit <strong>www.velmarcor-example.com/qms</strong> or <strong>Call +1 855 VELMARC</strong></p>
  <div class="company-name">Velmarcor</div>
</main>
</body>
</html>
```